Pocketly - New Payment App for Student

Pocket-ly - A Payment App for student to make payment, track own expenses and practice good dietary habits. The App theme is Fun and excitement.
Target User: Secondary Student aged 13-18
Look and Feel: Fun, excitement and simple.
Screen 1
Login to the app using thumbprints or password
Screen 2
Display the balance
Wallet balance >>> go to screen 3 to display transaction history
Gamification balance - points + badges >>> go to screen 3
Button to make payment
Screen 2-1
Allow them to do payment
Click “Pay”
Display QR code
scanning by merchant
Payment made
Notification received
The transaction history will be shown up
Screen 2-2
Allow them to top up (alternatively to parent Top-up using credit card)
Click “Top Up”
Display QR code
Pass the cash to merchant
scanning by merchant
Payment made
Notification received
The new balance will be shown up
Screen 3
Display more details on transaction history
Payment history + gamification history (gain/redeem points)
E.g. 14 Nov Canteen purchase $5.40
- Banana +30 points
- Milk +10 points
Screen 4 (play a game to earn point)
Introduce some trivial games (while waiting in line at cafeteria or school store) to gain some points
Crosswords
Puzzle
Screen 5 (Display achievements)
Leaderboard
Where the individual stands in the class
Where the class stands overall in school
Badges
Level
Achievements
For more, please go to our website http://www.pocketly.example/
Target Market(s)
Secondary School Student aged 13-18
Industry/Entity Type
Education
Logo Text
pocketly
Look and feel

```html
<!DOCTYPE html>
<html lang="en">
<head>
<meta charset="utf-8">
<title>Games</title>
<link rel="stylesheet" href="https://fonts.googleapis.com/css2?family=Fira+Sans:wght@400;500&display=swap">
<style>
  :root {
    --header-blue: #4499ee;
    --action-blue: #2b86ff;
    --points-blue: #2f86f0;
    --page-bg: #f1f1f1;
    --card-bg: #ffffff;
    --text-dark: #484848;
    --white: #ffffff;
    --coin-gold: #f2b51c;
    --coin-edge: #d08d0c;
    --art-dark: #1d1f30;
    --art-mid: #3b3e5c;
  }
  * { box-sizing: border-box; margin: 0; padding: 0; }
  html, body {
    width: 675px; height: 1200px; overflow: hidden;
    background: var(--page-bg);
    font-family: "Fira Sans", "Helvetica Neue", Arial, sans-serif;
  }
  .screen { position: relative; width: 675px; height: 1200px; overflow: hidden; }

  .app-bar {
    position: absolute; left: 0; top: 0; width: 675px; height: 141px;
    background: var(--header-blue); color: var(--white);
  }
  .status-bar {
    position: absolute; left: 0; top: 0; width: 100%; height: 38px;
    font-size: 19px; font-weight: 400; display: flex; align-items: center;
  }
  .status-bar .signal { position: absolute; left: 8px; top: 9px; }
  .status-bar .clock { position: absolute; left: 0; right: 0; padding-right: 18px; text-align: center; }
  .status-bar .battery-label { position: absolute; right: 63px; }
  .status-bar .battery { position: absolute; right: 10px; top: 9px; }
  .back-button { position: absolute; left: 30px; top: 70px; }
  .screen-title {
    position: absolute; left: 0; right: 0; top: 66px; padding-right: 24px;
    text-align: center; font-size: 39px; font-weight: 400; letter-spacing: 0.5px;
  }

  .game-card {
    position: absolute; background: var(--card-bg); border-radius: 11px; overflow: hidden;
  }
  .game-card.is-active {
    left: 86px; top: 324px; width: 503px; height: 699px;
    box-shadow: 0 14px 40px rgba(60, 90, 140, 0.16);
  }
  .game-card.is-peek-left { left: -470px; top: 393px; width: 506px; height: 588px; opacity: 0.9; }
  .game-card.is-peek-right { left: 639px; top: 393px; width: 506px; height: 588px; opacity: 0.9; }

  .game-art {
    width: 100%; height: 344px;
    background:
      radial-gradient(circle at 30% 45%, rgba(255,170,110,0.35), transparent 22%),
      radial-gradient(circle at 52% 65%, rgba(220,60,230,0.45), transparent 18%),
      radial-gradient(circle at 85% 80%, rgba(60,230,200,0.35), transparent 22%),
      radial-gradient(circle at 60% 20%, rgba(255,90,150,0.3), transparent 20%),
      linear-gradient(160deg, var(--art-mid) 0%, var(--art-dark) 55%, #14151f 100%);
  }
  .is-peek-left .game-art, .is-peek-right .game-art {
    height: 289px;
    background: linear-gradient(160deg, #c9ced8 0%, #aeb6c4 60%, #9ea8b8 100%);
  }

  .game-info { padding: 26px 26px 0 32px; color: var(--text-dark); }
  .game-title { font-size: 36px; font-weight: 400; letter-spacing: 0.4px; line-height: 1.1; }
  .points-row {
    margin-top: 30px; display: flex; align-items: center; justify-content: space-between;
  }
  .points-label { font-size: 29px; }
  .points-value {
    display: flex; align-items: center; gap: 8px;
    color: var(--points-blue); font-size: 38px;
  }
  .play-button {
    position: absolute; left: 102px; top: 598px; width: 299px; height: 63px;
    border-radius: 32px; background: var(--action-blue); color: var(--white);
    border: none; font-family: inherit; font-size: 30px; letter-spacing: 0.5px;
    box-shadow: 0 10px 22px rgba(43, 134, 255, 0.3);
  }
</style>
</head>
<body>
<main class="screen">
  <header class="app-bar">
    <div class="status-bar">
      <svg class="signal" width="95" height="20" viewBox="0 0 95 20" aria-hidden="true">
        <g fill="#fff"><circle cx="6" cy="8" r="5"/><circle cx="19" cy="8" r="5"/><circle cx="32" cy="8" r="5"/><circle cx="45" cy="8" r="5"/><circle cx="58" cy="8" r="5"/></g>
        <path d="M68 5 a14 14 0 0 1 20 0 M71 9 a9 9 0 0 1 14 0" stroke="#fff" stroke-width="2.4" fill="none"/>
        <circle cx="78" cy="13" r="2.5" fill="#fff"/>
      </svg>
      <span class="clock">9:41 AM</span>
      <span class="battery-label">100%</span>
      <svg class="battery" width="48" height="20" viewBox="33 0 47 20" aria-hidden="true">
        <rect x="34" y="1" width="39" height="18" rx="3" fill="none" stroke="#fff" stroke-width="2"/>
        <rect x="37" y="4" width="33" height="12" rx="1.5" fill="#fff"/>
        <rect x="75" y="7" width="3" height="6" rx="1" fill="#fff"/>
      </svg>
    </div>
    <svg class="back-button" width="48" height="36" viewBox="0 0 48 36" aria-label="Back" role="img">
      <path d="M46 18 H5 M19 4 L4 18 L19 32" stroke="#fff" stroke-width="4.5" fill="none" stroke-linecap="round" stroke-linejoin="round"/>
    </svg>
    <h1 class="screen-title">Games</h1>
  </header>

  <article class="game-card is-peek-left" aria-hidden="true">
    <div class="game-art" role="img" aria-label="Game artwork"></div>
  </article>

  <article class="game-card is-active">
    <div class="game-art" role="img" aria-label="Isometric night city illustration with neon-lit buildings"></div>
    <div class="game-info">
      <h2 class="game-title">The Real Trivia</h2>
      <div class="points-row">
        <span class="points-label">Points Earned</span>
        <span class="points-value">40
          <svg width="42" height="42" viewBox="0 0 42 42" aria-hidden="true">
            <g stroke="var(--coin-edge)" stroke-width="1.5" fill="var(--coin-gold)">
              <ellipse cx="23" cy="33" rx="17" ry="6"/>
              <ellipse cx="21" cy="26" rx="17" ry="6"/>
              <ellipse cx="23" cy="19" rx="17" ry="6"/>
              <ellipse cx="21" cy="11" rx="14" ry="8"/>
            </g>
            <circle cx="21" cy="11" r="4" fill="var(--coin-edge)"/>
          </svg>
        </span>
      </div>
    </div>
    <button class="play-button" type="button">Play</button>
  </article>

  <article class="game-card is-peek-right" aria-hidden="true">
    <div class="game-art" role="img" aria-label="Game artwork"></div>
  </article>
</main>
</body>
</html>
```